Buff & Gleam

polished concrete and epoxy coatings flooring company

Target Market(s)

Industrial commercial

Industry/Entity Type

Industrial flooring contractor

Contact Information for Business Card

POLISHED CONCRETE • EPOXY COATING • TERRAZZO RESTORATION • SHOT BLASTING • SURFACE PREPARATION • JOINT FILLING • TILE/ CARPET /GLUE REMOVAL

Colors
0054AA
0677BA
7BADD7
CADEEF
E8F1F8

Requirements
Must have
• email buffandgleamfloors@mailbrook.example Address 47215 Tallowmere Rd, Fraser, MI 48093. Name Ray Tulvin. Services Polished concrete- Epoxy Coatings- Terrazzo restoration-surface preparation- safety striping- joint filling- tile/ carpet/ glue removal phone number 586-700-3926 email buffandgleamfloors.example
Nice to have
• Instagram Facebook logo maybe smaller in the corner

```html
<!DOCTYPE html>
<html lang="en">
<head>
<meta charset="utf-8">
<title>Buff &amp; Gleam — Business Card</title>
<link rel="stylesheet" href="https://fonts.googleapis.com/css2?family=Archivo:wght@400;600&family=Oswald:wght@500&display=swap">
<style>
  :root {
    --canvas-bg: #e6f4fb;
    --card-white: #ffffff;
    --brand-blue: #3385b0;
    --ink-blue: #2f86b4;
    --accent-cyan: #4fb8e6;
    --text-white: #ffffff;
  }
  * { box-sizing: border-box; margin: 0; padding: 0; }
  html, body { width: 1200px; height: 800px; overflow: hidden; }
  body { background: var(--canvas-bg); position: relative; }

  .card { position: absolute; width: 281px; height: 450px; overflow: hidden; }

  /* Front: contact side */
  .card-front { left: 206px; top: 172px; background: var(--card-white); }
  .terrazzo-field {
    position: absolute; left: 0; top: 0; width: 100%; height: 258px;
    background: linear-gradient(180deg, rgba(183,166,220,0.35) 0%, rgba(111,183,163,0.22) 55%, rgba(255,255,255,0) 100%);
  }
  .contact-name {
    position: absolute; left: 31px; top: 283px;
    font-family: "Archivo", sans-serif; font-weight: 600; font-size: 28px;
    color: var(--ink-blue); letter-spacing: -0.2px;
  }
  .contact-list {
    position: absolute; left: 31px; top: 332px; list-style: none;
    font-family: "Archivo", sans-serif; font-size: 12.5px; line-height: 16px;
    color: var(--ink-blue);
  }
  .contact-list li { position: relative; padding-left: 11px; margin-bottom: 4px; }
  .contact-list li::before {
    content: ""; position: absolute; left: 0; top: 6px;
    width: 4px; height: 4px; border-radius: 50%; background: var(--accent-cyan);
  }

  /* Back: brand side */
  .card-back { left: 659px; top: 122px; background: var(--brand-blue); color: var(--text-white); }
  .terrazzo-band {
    position: absolute; left: 0; top: 0; width: 100%; height: 140px;
    background: linear-gradient(180deg, rgba(255,255,255,0.22) 0%, rgba(79,184,230,0.18) 50%, rgba(51,133,176,0) 100%);
  }
  .brand-name {
    position: absolute; left: 0; top: 160px; width: 100%; text-align: center;
    font-family: "Oswald", sans-serif; font-weight: 500; font-size: 46px; line-height: 54px;
    letter-spacing: 1px; color: var(--text-white);
  }
  .tagline {
    position: absolute; left: 0; top: 280px; width: 100%; text-align: center;
    font-family: "Oswald", sans-serif; font-weight: 500; font-size: 14px; letter-spacing: 0.1px;
  }
  .divider { position: absolute; left: 102px; top: 338px; width: 76px; height: 2px; background: var(--text-white); }
  .services {
    position: absolute; left: 12px; top: 366px; width: 257px; text-align: center;
    font-family: "Oswald", sans-serif; font-weight: 500; font-size: 9.6px; line-height: 20px;
  }
  .services .dot { color: var(--accent-cyan); margin: 0 2px; }
</style>
</head>
<body>

  <section class="card card-front" aria-label="Business card front">
    <div class="terrazzo-field" role="img" aria-label="Scattered terrazzo chip pattern in blue, lilac and teal"></div>
    <h1 class="contact-name">Ray Tulvin</h1>
    <ul class="contact-list">
      <li>586-700-3926</li>
      <li>buffandgleamfloors@mailbrook.example</li>
      <li>buffandgleamfloors.example</li>
      <li>47215 Tallowmere Rd,<br>Fraser, MI 48093</li>
    </ul>
  </section>

  <section class="card card-back" aria-label="Business card back">
    <div class="terrazzo-band" role="img" aria-label="Scattered white and light blue terrazzo chip pattern"></div>
    <p class="brand-name">BUFF &amp;<br>GLEAM</p>
    <p class="tagline">INNOVATIVE CONCRETE FLOORING</p>
    <div class="divider"></div>
    <p class="services">
      <span class="dot">•</span> POLISHED CONCRETE <span class="dot">•</span> EPOXY COATING <span class="dot">•</span> TERRAZZO<br>
      RESTORATION <span class="dot">•</span> SHOT BLASTING <span class="dot">•</span> SURFACE PREPARATION <span class="dot">•</span><br>
      <span class="dot">•</span> JOINT FILLING <span class="dot">•</span> TILE/ CARPET /GLUE REMOVAL <span class="dot">•</span>
    </p>
  </section>

</body>
</html>
```